Need DL Flyer for Real Estate Drops

We need a real estate flyer ,double sided. With content on 1 side like: Want to know what's your house is worth " contact us today and on other side agent details. We are looking for an ongoing partnership with designer so this assignment will be ongoing

```html
<!DOCTYPE html>
<html lang="en">
<head>
<meta charset="utf-8">
<title>Meridian Real Estate – DL Flyer</title>
<link rel="stylesheet" href="https://fonts.googleapis.com/css2?family=Barlow:wght@300;400;600;700&display=swap">
<style>
  :root {
    --navy: #0c1733;
    --red: #c8202a;
    --red-deep: #8e0f16;
    --white: #ffffff;
    --canvas: #ebecee;
    --sky: #d9d9ea;
    --slate: #46557c;
  }
  * { box-sizing: border-box; margin: 0; padding: 0; }
  html, body { width: 1200px; height: 1200px; overflow: hidden; }
  body {
    background: var(--canvas);
    font-family: "Barlow", Arial, sans-serif;
    color: var(--white);
    position: relative;
  }
  .flyer {
    position: absolute;
    top: 90px;
    width: 496px;
    height: 1020px;
    background: var(--navy);
    overflow: hidden;
  }
  .flyer--front { left: 67px; }
  .flyer--back { left: 628px; }
  .abs { position: absolute; }

  /* shared bits */
  .brand {
    display: flex;
    align-items: center;
    gap: 14px;
  }
  .brand__mark { width: 40px; height: 40px; background: var(--red); flex: none; }
  .brand__name {
    font-weight: 600;
    color: var(--navy);
    white-space: nowrap;
    letter-spacing: 0.5px;
  }
  .icon {
    border-radius: 50%;
    background: var(--white);
    display: flex;
    align-items: center;
    justify-content: center;
    flex: none;
  }
  .icon svg { display: block; }
  .detail-line {
    display: flex;
    align-items: center;
    gap: 14px;
    font-weight: 400;
    white-space: nowrap;
  }

  /* front */
  .hero-photo {
    left: 0; top: 0; width: 496px; height: 540px;
    background: linear-gradient(180deg, var(--sky) 0%, #c9c6e0 30%, var(--slate) 62%, #5c6a8c 100%);
  }
  .front-brand { left: 88px; top: 64px; }
  .front-brand .brand__mark { width: 52px; height: 52px; }
  .front-brand .brand__name { font-size: 36px; }
  .band { left: 0; top: 0; }
  .headline {
    left: 44px; top: 534px;
    text-transform: uppercase;
    line-height: 43px;
    font-size: 40px;
  }
  .headline__lead { font-weight: 300; }
  .headline__main { font-weight: 700; }
  .contact-label {
    font-weight: 400;
    font-size: 20px;
    text-transform: uppercase;
    letter-spacing: 0.5px;
  }
  .front-contact-label { left: 43px; top: 707px; }
  .big-phone {
    left: 42px;
    display: flex; align-items: center; gap: 16px;
    font-weight: 600; font-size: 42px; letter-spacing: 0.3px;
  }
  .big-phone .icon { width: 40px; height: 40px; }
  .big-phone--office { top: 745px; }
  .big-phone--mobile { top: 804px; }
  .divider { left: 42px; top: 876px; width: 296px; height: 2px; background: var(--red); }
  .front-details { left: 38px; top: 900px; display: flex; flex-direction: column; gap: 9px; font-size: 14px; }

  /* back */
  .portrait {
    left: 151px; top: 50px; width: 345px; height: 470px;
    border-radius: 0 0 0 160px;
    background: linear-gradient(160deg, #8d6a5a 0%, #2a3b78 45%, #1d2c5e 100%);
  }
  .agent-name {
    left: 48px; top: 548px;
    font-weight: 700; font-size: 44px; text-transform: uppercase; letter-spacing: 0.5px;
  }
  .agent-role {
    left: 48px; top: 604px;
    font-weight: 300; font-size: 20px; line-height: 24px; text-transform: uppercase;
  }
  .back-contact-label { left: 49px; top: 711px; }
  .phone-row {
    left: 48px; top: 752px;
    display: flex; gap: 40px;
    font-weight: 600; font-size: 25px;
  }
  .phone-row .detail-line { gap: 10px; font-weight: 600; }
  .back-details .icon, .phone-row .icon { width: 25px; height: 25px; }
  .back-details { left: 48px; top: 798px; display: flex; flex-direction: column; gap: 20px; font-size: 17px; }
  .back-details .detail-line { gap: 12px; }
  .footer {
    left: 0; top: 889px; width: 496px; height: 131px;
    background: var(--white);
    border-top-right-radius: 95px;
  }
  .footer-brand { left: 33px; top: 36px; gap: 12px; }
  .footer-brand .brand__mark { width: 44px; height: 44px; }
  .footer-brand .brand__name { font-size: 21px; line-height: 23px; }
  .footer-details {
    left: 247px; top: 22px;
    color: var(--navy); font-size: 15px; line-height: 20px;
    display: flex; flex-direction: column; gap: 10px;
  }
  .footer-details .detail-line { align-items: flex-start; gap: 10px; }
  .footer-details svg { margin-top: 3px; }
</style>
</head>
<body>

<!-- FRONT -->
<section class="flyer flyer--front">
  <div class="abs hero-photo" role="img" aria-label="Photo of a two-storey suburban home at dusk with a magnifying glass revealing a gold dollar sign"></div>

  <div class="abs brand front-brand">
    <span class="brand__mark"></span>
    <span class="brand__name">Meridian Real Estate</span>
  </div>

  <svg class="abs band" width="496" height="1020" viewBox="0 0 496 1020" aria-hidden="true">
    <defs>
      <linearGradient id="bandShade" x1="0" x2="1" y1="0" y2="0">
        <stop offset="0" stop-color="#c8202a"/>
        <stop offset="0.6" stop-color="#b81a24"/>
        <stop offset="1" stop-color="#8e0f16"/>
      </linearGradient>
    </defs>
    <path d="M0 516 H496 V640 C440 668 380 681 300 681 H0 Z" fill="url(#bandShade)"/>
  </svg>

  <h1 class="abs headline">
    <span class="headline__lead">Want to know</span><br>
    <span class="headline__main">What's your house<br>is worth</span>
  </h1>

  <p class="abs contact-label front-contact-label">Contact us today</p>

  <div class="abs big-phone big-phone--office">
    <span class="icon">
      <svg width="22" height="22" viewBox="0 0 24 24" fill="none" stroke="#c8202a" stroke-width="1.8" stroke-linecap="round" stroke-linejoin="round"><path d="M22 16.9v3a2 2 0 0 1-2.2 2 19.8 19.8 0 0 1-8.6-3.1 19.5 19.5 0 0 1-6-6A19.8 19.8 0 0 1 2.1 4.2 2 2 0 0 1 4.1 2h3a2 2 0 0 1 2 1.7c.1.9.4 1.8.7 2.7a2 2 0 0 1-.5 2.1L8 9.8a16 16 0 0 0 6 6l1.3-1.3a2 2 0 0 1 2.1-.4c.9.3 1.8.6 2.7.7a2 2 0 0 1 1.7 2z"/></svg>
    </span>
    <span>03 5550 1234</span>
  </div>
  <div class="abs big-phone big-phone--mobile">
    <span class="icon">
      <svg width="20" height="22" viewBox="0 0 24 24" fill="none" stroke="#c8202a" stroke-width="1.8" stroke-linecap="round"><rect x="6" y="2" width="12" height="20" rx="2"/><path d="M11 18h2"/></svg>
    </span>
    <span>04 0000 5512</span>
  </div>

  <div class="abs divider"></div>

  <div class="abs front-details">
    <div class="detail-line">
      <svg width="12" height="12" viewBox="0 0 24 24" fill="none" stroke="#c8202a" stroke-width="2"><path d="M12 22s7-6.5 7-12a7 7 0 0 0-14 0c0 5.5 7 12 7 12z"/><circle cx="12" cy="10" r="2.5"/></svg>
      <span>14/8 Harbour Lane, Westvale 3040</span>
    </div>
    <div class="detail-line">
      <svg width="12" height="12" viewBox="0 0 24 24" fill="none" stroke="#c8202a" stroke-width="2"><rect x="3" y="5" width="18" height="14" rx="1.5"/><path d="M3 6l9 7 9-7"/></svg>
      <span>daniel@meridianhomes.com.au</span>
    </div>
    <div class="detail-line">
      <svg width="12" height="12" viewBox="0 0 24 24" fill="none" stroke="#c8202a" stroke-width="2"><circle cx="12" cy="12" r="9"/><path d="M3 12h18M12 3c3 3 3 15 0 18M12 3c-3 3-3 15 0 18"/></svg>
      <span>www.meridianhomes.com.au</span>
    </div>
  </div>
</section>

<!-- BACK -->
<section class="flyer flyer--back">
  <div class="abs portrait" role="img" aria-label="Portrait photo of the agent in a navy suit and striped tie"></div>

  <svg class="abs band" width="496" height="1020" viewBox="0 0 496 1020" aria-hidden="true">
    <path d="M0 519 H496 V630 C430 662 370 681 300 681 H0 Z" fill="#c8202a"/>
  </svg>

  <h2 class="abs agent-name">Daniel Varma</h2>
  <p class="abs agent-role">Managing Director/LEA,<br>Meridian Real Estate</p>

  <p class="abs contact-label back-contact-label">Contact</p>

  <div class="abs phone-row">
    <div class="detail-line">
      <span class="icon">
        <svg width="14" height="14" viewBox="0 0 24 24" fill="none" stroke="#c8202a" stroke-width="2" stroke-linecap="round" stroke-linejoin="round"><path d="M22 16.9v3a2 2 0 0 1-2.2 2 19.8 19.8 0 0 1-8.6-3.1 19.5 19.5 0 0 1-6-6A19.8 19.8 0 0 1 2.1 4.2 2 2 0 0 1 4.1 2h3a2 2 0 0 1 2 1.7c.1.9.4 1.8.7 2.7a2 2 0 0 1-.5 2.1L8 9.8a16 16 0 0 0 6 6l1.3-1.3a2 2 0 0 1 2.1-.4c.9.3 1.8.6 2.7.7a2 2 0 0 1 1.7 2z"/></svg>
      </span>
      <span>03 5550 1234</span>
    </div>
    <div class="detail-line">
      <span class="icon">
        <svg width="13" height="14" viewBox="0 0 24 24" fill="none" stroke="#c8202a" stroke-width="2" stroke-linecap="round"><rect x="6" y="2" width="12" height="20" rx="2"/><path d="M11 18h2"/></svg>
      </span>
      <span>04 0000 5512</span>
    </div>
  </div>

  <div class="abs back-details">
    <div class="detail-line">
      <span class="icon">
        <svg width="13" height="13" viewBox="0 0 24 24" fill="none" stroke="#c8202a" stroke-width="2"><rect x="3" y="5" width="18" height="14" rx="1.5"/><path d="M3 6l9 7 9-7"/></svg>
      </span>
      <span>daniel@meridianhomes.com.au</span>
    </div>
    <div class="detail-line">
      <span class="icon">
        <svg width="13" height="13" viewBox="0 0 24 24" fill="none" stroke="#c8202a" stroke-width="2" stroke-linecap="round"><circle cx="12" cy="8" r="4"/><path d="M4 21c0-4.4 3.6-7 8-7s8 2.6 8 7"/></svg>
      </span>
      <span>danielvarmaMRE</span>
    </div>
  </div>

  <div class="abs footer">
    <div class="abs brand footer-brand">
      <span class="brand__mark"></span>
      <span class="brand__name">Meridian<br>Real Estate</span>
    </div>
    <div class="abs footer-details">
      <div class="detail-line">
        <svg width="12" height="14" viewBox="0 0 24 24" fill="none" stroke="#c8202a" stroke-width="2"><path d="M12 22s7-6.5 7-12a7 7 0 0 0-14 0c0 5.5 7 12 7 12z"/><circle cx="12" cy="10" r="2.5"/></svg>
        <span>14/8 Harbour Lane,<br>Westvale 3040</span>
      </div>
      <div class="detail-line">
        <svg width="13" height="14" viewBox="0 0 24 24" fill="none" stroke="#c8202a" stroke-width="2"><circle cx="12" cy="12" r="9"/><path d="M3 12h18M12 3c3 3 3 15 0 18M12 3c-3 3-3 15 0 18"/></svg>
        <span>www.meridianhomes.com.au</span>
      </div>
    </div>
  </div>
</section>

</body>
</html>
```